Hope KLN Disease (Non-Profit) Tri-Fold Brochure Design

We have put together the content for a brochure that we will distribute to doctors, researchers and patients about our non-profit. We would like the design of the brochure to look more professional and have nice aesthetics. It needs to incorporate all of the content in the attached Word file. We will have printed once we have a finished design.

Target Market(s)

Medical

Industry/Entity Type

Non Profit

Font styles to use
Serif
Sans Serif

Colors
33a6d7

Requirements
Must have
• Must include all content provided. Professional.
Nice to have
• Colors

```html
<!DOCTYPE html>
<html lang="en">
<head>
<meta charset="utf-8">
<title>Hope KLN Disease – Tri-Fold Brochure</title>
<link href="https://fonts.googleapis.com/css2?family=Montserrat:wght@300;400;600;700;800&family=Roboto+Condensed:wght@400;700&display=swap" rel="stylesheet">
<style>
  :root{
    --blue:#1a9ad9;
    --blue-deep:#0e86d0;
    --brand:#33a6d7;
    --orange:#f58a34;
    --ink:#222;
    --grey:#5a5a5a;
    --grey-light:#b9b9b9;
    --teal:#2bb1c4;
    --white:#fff;
  }
  *{margin:0;padding:0;box-sizing:border-box}
  html,body{width:1200px;height:928px;overflow:hidden;background:#fff}
  .brochure{position:relative;width:1200px;height:928px;overflow:hidden;background:#fff;font-family:"Roboto Condensed",Arial,sans-serif;color:var(--ink)}
  .panel{position:absolute;top:0;width:400px;height:928px}
  .panel--left{left:0}
  .panel--mid{left:400px}
  .panel--right{left:800px;width:400px}
  .abs{position:absolute}
  .header-band{position:absolute;top:0;left:0;width:400px;height:156px;background:linear-gradient(90deg,var(--blue-deep),var(--blue))}
  .panel--mid .header-band{background:var(--blue)}
  .header-title{position:absolute;left:48px;top:98px;font-family:"Montserrat",sans-serif;font-weight:700;font-size:27px;color:var(--white)}
  .tagline{position:absolute;left:0;width:400px;text-align:center;font-family:"Montserrat",sans-serif;font-weight:300;color:var(--white)}
  .tagline--main{top:42px;font-size:37px;letter-spacing:.5px}
  .tagline--sub{top:86px;font-size:24px}
  .body-text{font-size:15.5px;line-height:19px;text-align:justify;color:#1d1d1d}
  .body-text p+p{margin-top:6px}
  .section-title{font-family:"Montserrat",sans-serif;font-weight:800;color:var(--blue);line-height:25px;font-size:26px}
  .def{font-size:15px;line-height:30px}
  .def b{font-weight:700}
  .pie-label{font-family:Arial,sans-serif;font-size:8.5px;font-weight:700;fill:#222}
  .org-name{font-family:"Montserrat",sans-serif;font-weight:600}
  .offer{left:40px;width:320px;top:550px;text-align:center;font-weight:700;color:var(--blue);font-size:14px;line-height:21px}
  .connect{left:0;width:400px;top:598px;text-align:center;font-family:"Montserrat",sans-serif;font-weight:700;font-size:25px;color:var(--grey-light);letter-spacing:1px}
  .social-band{left:0;top:630px;width:400px;height:38px;background:var(--orange);color:#fff;font-weight:700;font-size:14.5px;display:flex;align-items:center;justify-content:center;gap:14px}
  .contact-block{left:0;top:672px;width:400px;height:160px;background:var(--blue);color:#fff;font-family:"Montserrat",sans-serif;font-size:15px}
  .contact-row{position:absolute;left:90px}
  .contact-icon{position:absolute;left:-36px}
  .rule{position:absolute;left:90px;width:200px;border-top:1px dashed rgba(255,255,255,.8)}
  .photo-bg{position:absolute;inset:0;background:
      radial-gradient(ellipse at 80% 15%,rgba(255,255,255,.9),rgba(255,255,255,0) 60%),
      linear-gradient(180deg,#e9f2f7 0%,#f3f7fa 45%,#bfe0f1 70%,#6fbde6 100%)}
  .q{position:absolute;left:48px;font-family:"Montserrat",sans-serif;line-height:1}
  .q--blue{color:var(--blue);font-weight:400;font-size:24px}
  .q--grey{color:var(--grey);font-weight:800;font-size:28px}
  .right-copy{position:absolute;right:33px;text-align:right;font-family:"Montserrat",sans-serif;color:#222}
</style>
</head>
<body>
<div class="brochure">

  <!-- LEFT PANEL -->
  <section class="panel panel--left">
    <div class="header-band"></div>
    <h2 class="header-title">What is IBMPFD?</h2>

    <div class="abs body-text" style="left:47px;top:184px;width:312px">
      <p>Inclusion Body Myopathy associated with Paget's disease of bone and Frontotemporal Dementia is an autosomal dominant mutation in chromosome 9 of the <i>VCP (Valosin Containing Protein)</i> gene. Given the interaction with other genetic diseases, this mutation may also be known as <i>VCP</i> Disease or Disorder.</p>
      <p>Some patients have familial Amyotrophic Lateral Sclerosis (ALS or Lou Gehrig's disease) or Parkinson's which has been shown to have a pathogenic variant in <i>VCP</i>.</p>
    </div>

    <h3 class="abs section-title" style="left:46px;top:441px">PENETRANCE BY<br>PHENOTYPE</h3>
    <p class="abs" style="left:47px;top:504px;width:340px;font-size:15px;line-height:20px">The frequency that IBMPFD or <i>VCP</i> Disease manifests itself in one, two, or three primary disorders.</p>
    <div class="abs def" style="left:47px;top:553px">
      <div><b>IBM</b> : Inclusion Body Myopathy</div>
      <div><b>PDB</b> :&nbsp; Paget's Disease of the Bone</div>
      <div><b>FTD</b> : Frontotemporal Dementia</div>
    </div>

    <svg class="abs" style="left:0;top:0" width="400" height="928" viewBox="0 0 400 928" aria-label="Pie chart of penetrance by phenotype">
      <!-- depth -->
      <path d="M67 772 A135 68 0 0 0 103.6 818.6 L103.6 842.6 A135 68 0 0 1 67 796 Z" fill="#c99a00"/>
      <path d="M103.6 818.6 A135 68 0 0 0 337 772 L337 796 A135 68 0 0 1 103.6 842.6 Z" fill="#6d6d6d"/>
      <!-- slices -->
      <path d="M202 772 L202 704 A135 68 0 0 1 281.4 717 Z" fill="#3f63c4"/>
      <path d="M202 772 L281.4 717 A135 68 0 0 1 336.7 776.3 Z" fill="#ef7d2a"/>
      <path d="M202 772 L336.7 776.3 A135 68 0 0 1 103.6 818.6 Z" fill="#a6a6a6"/>
      <path d="M202 772 L103.6 818.6 A135 68 0 0 1 122.6 717 Z" fill="#fbbd0b"/>
      <path d="M202 772 L122.6 717 A135 68 0 0 1 129.6 714.6 Z" fill="#4aa1df"/>
      <path d="M202 772 L129.6 714.6 A135 68 0 0 1 168.4 706.1 Z" fill="#6aa842"/>
      <path d="M202 772 L168.4 706.1 A135 68 0 0 1 202 704 Z" fill="#1f3a73"/>
      <!-- leaders -->
      <g stroke="#555" stroke-width=".7" fill="none">
        <polyline points="86,722 142,722 132,716"/>
        <polyline points="153,708 153,712"/>
        <polyline points="192,700 192,710"/>
        <polyline points="290,716 290,716"/>
        <polyline points="250,716 288,716"/>
        <polyline points="300,745 351,760"/>
        <polyline points="57,760 62,780 80,790"/>
        <polyline points="245,860 250,902 296,902"/>
      </g>
      <g>
        <circle cx="86" cy="722" r="2.5" fill="#4aa1df"/>
        <circle cx="153" cy="706" r="2.5" fill="#6aa842"/>
        <circle cx="192" cy="701" r="2.5" fill="#1f3a73"/>
        <circle cx="289" cy="716" r="2.5" fill="#3f63c4"/>
        <circle cx="351" cy="760" r="2.5" fill="#ef7d2a"/>
        <circle cx="57" cy="760" r="2.5" fill="#fbbd0b"/>
        <circle cx="296" cy="902" r="2.5" fill="#555"/>
      </g>
      <text class="pie-label" x="62" y="714">PDB &amp; FTD</text>
      <text class="pie-label" x="62" y="726">1%</text>
      <text class="pie-label" x="128" y="699">PDB only</text>
      <text class="pie-label" x="128" y="711">5%</text>
      <text class="pie-label" x="177" y="691">FTD only</text>
      <text class="pie-label" x="202" y="704">3%</text>
      <text class="pie-label" x="253" y="707">IBM,PDB &amp; FTD</text>
      <text class="pie-label" x="300" y="719">10%</text>
      <text class="pie-label" x="335" y="752">IBM &amp; FTD</text>
      <text class="pie-label" x="362" y="765">16%</text>
      <text class="pie-label" x="31" y="752">IBM &amp; PDB</text>
      <text class="pie-label" x="31" y="764">27%</text>
      <text class="pie-label" x="283" y="891">IBM only</text>
      <text class="pie-label" x="301" y="904">37%</text>
    </svg>
  </section>

  <!-- MIDDLE PANEL -->
  <section class="panel panel--mid">
    <div class="header-band"></div>
    <div class="tagline tagline--main">Together We Can</div>
    <div class="tagline tagline--sub">Make a Difference</div>

    <h3 class="abs section-title" style="left:36px;top:180px;font-size:27px">PATIENT SUPPORT</h3>
    <div class="abs body-text" style="left:36px;top:228px;width:328px;font-size:15px;line-height:19px">
      <p>Hope KLN Disease, Inc. is a 501(c)(3) which was formed to drive efforts to cure diseases related to mutations of the Valosin Containing Protein (VCP) gene. Our main goal is to bring patients and doctors together so we can help one another and drive research towards a cure.</p>
      <p>We are also trying to bring awareness to the medical community about our rare disease. Currently, there are less than 500 people diagnosed worldwide.</p>
    </div>

    <div class="abs" style="left:0;width:400px;top:455px;display:flex;justify-content:center;align-items:center;gap:10px">
      <span style="width:16px;height:16px;border-radius:50%;background:var(--teal);display:block"></span>
      <span class="org-name" style="font-size:26px;color:var(--teal)">Hope KLN Disease</span>
    </div>

    <p class="abs offer">We offer resources and support to patients,caregivers and doctors.</p>
    <div class="abs connect">CONNECT WITH US</div>
    <div class="abs social-band"><span>IBMPFD Community page</span><span>|</span><span>IBMPFDinfo.org</span></div>

    <div class="abs contact-block">
      <div class="contact-row" style="top:22px;line-height:22px">
        <svg class="contact-icon" style="top:2px" width="20" height="24" viewBox="0 0 20 24" aria-hidden="true"><path d="M10 1a8 8 0 0 0-8 8c0 6 8 14 8 14s8-8 8-14a8 8 0 0 0-8-8z" fill="#fff"/><circle cx="10" cy="9" r="3" fill="var(--blue)"/></svg>
        Hope KLN Disease, Inc.P.O. Box 4120<br>Lakeview, GA 31999
      </div>
      <div class="rule" style="top:75px"></div>
      <div class="contact-row" style="top:84px">
        <svg class="contact-icon" style="top:2px" width="22" height="16" viewBox="0 0 22 16" aria-hidden="true"><rect x="1" y="1" width="20" height="14" fill="none" stroke="#fff" stroke-width="1.6"/><path d="M1 1l10 8 10-8" fill="none" stroke="#fff" stroke-width="1.6"/></svg>
        hopeklndisease@mailbox.org
      </div>
      <div class="rule" style="top:114px"></div>
      <div class="contact-row" style="top:128px;font-weight:700;font-style:italic;font-size:17px">
        <svg class="contact-icon" style="top:3px" width="20" height="20" viewBox="0 0 20 20" aria-hidden="true"><g fill="none" stroke="#fff" stroke-width="1.4"><circle cx="10" cy="10" r="8.5"/><ellipse cx="10" cy="10" rx="4" ry="8.5"/><path d="M1.5 10h17M3 5.5h14M3 14.5h14"/></g></svg>
        www.hopekln.org
      </div>
    </div>

    <div class="abs" role="img" aria-label="Partner badge" style="left:165px;top:846px;width:70px;height:64px;border-radius:8px;background:#dbe7ee"></div>
  </section>

  <!-- RIGHT PANEL -->
  <section class="panel panel--right">
    <div class="photo-bg" role="img" aria-label="Soft-focus laboratory scene with gloved hands and test tubes"></div>

    <svg class="abs" style="left:0;top:0" width="400" height="928" viewBox="0 0 400 928" aria-hidden="true">
      <path d="M0 420 C40 560 150 620 300 640 L300 646 C130 640 20 580 0 500 Z" fill="#123f8f"/>
      <path d="M0 320 C30 500 150 600 300 640 C120 615 20 540 0 470 Z" fill="#1a8fe0"/>
      <path d="M0 380 C30 560 170 630 300 645 C150 670 30 620 0 560 Z" fill="var(--orange)"/>
      <path d="M170 0 C60 140 30 300 0 380 L0 0 Z" fill="rgba(255,255,255,.35)"/>
    </svg>

    <div class="abs" style="left:51px;top:44px;font-family:'Montserrat',sans-serif;font-size:20px;line-height:26px;color:#333">Do you have a family<br>history of ADULT ONSET</div>
    <div class="q q--blue" style="top:112px">Muscle Weakness?</div>
    <div class="q q--grey" style="top:134px">Dementia?</div>
    <div class="q q--blue" style="top:164px">Bone Disease?</div>
    <div class="q q--grey" style="top:186px">ALS?</div>
    <div class="q q--blue" style="top:216px">Parkinson's?</div>
    <div class="q q--grey" style="top:238px">IBM?</div>

    <div class="right-copy" style="top:306px;font-size:22px;line-height:26px">You may consider talking<br>to your doctor about<br>a mutation of the <i>VCP</i><br>gene called</div>
    <div class="right-copy" style="top:422px;font-size:36px;font-weight:800;color:var(--blue)">IBMPFD</div>
    <div class="right-copy" style="top:480px;font-size:17px;line-height:26px">Inclusion Body Myopathy<br>associated with Paget's<br>Disease of Bone and<br>Frontotemporal<br>Dementia.</div>

    <div class="abs" style="left:40px;top:740px;display:flex;align-items:center;gap:12px">
      <span style="width:22px;height:22px;border-radius:50%;background:#fff;display:block"></span>
      <span class="org-name" style="font-size:31px;color:#fff">Hope KLN Disease</span>
    </div>
    <div class="right-copy" style="top:876px;font-size:17px;font-weight:700;font-style:italic;color:#fff">www.hopekln.org</div>
  </section>

</div>
</body>
</html>
```